A3 Menus for new international restaurant in Singapore.

Looking for new A3 menu design for indoor & outdoor (beautiful garden and trees) restaurant that caters for expat and local families. International menu, cool jazz vibe, great for couples and families. Restaurant called Brass Cove Parlour. I have attached some of the logos we use. Will consider black and white or color options. Restaurant located on a hill where there were tin mines many years ago, hence the name and branding. Looking for three menus (1) Dinner (2) Lunch (3) weekend brunch.

Target Market(s)

Families, young couples and professionals.

Industry/Entity Type

Restaurant

Font styles to use
Serif
Sans Serif

Requirements
Must have
• All food layout on one side of A3, one for each attached menu. Also a space for drinks list on the back.
Nice to have
• Use some of the logo material we have attached.
Should not have

```html
<!DOCTYPE html>
<html lang="en">
<head>
<meta charset="utf-8">
<title>Brass Cove Parlour – Dinner Menu</title>
<link href="https://fonts.googleapis.com/css2?family=Special+Elite&family=Crimson+Text:ital,wght@0,400;0,600;1,400&display=swap" rel="stylesheet">
<style>
  :root {
    --bg: #2b211b;
    --rust: #a2602f;
    --rust-light: #b8773f;
    --rust-dark: #6d3a1c;
    --paper: #f4f2ee;
    --cream: #f1e6d4;
    --heading: #a9541f;
    --ink: #3b2b21;
    --ghost: rgba(241, 222, 196, 0.16);
  }
  * { box-sizing: border-box; margin: 0; padding: 0; }
  html, body { width: 1200px; height: 1000px; overflow: hidden; background: var(--bg); }
  body { position: relative; font-family: "Crimson Text", Georgia, serif; color: var(--ink); }

  .rust-surface {
    background:
      radial-gradient(ellipse at 30% 20%, rgba(196,130,70,.55), transparent 60%),
      radial-gradient(ellipse at 75% 70%, rgba(120,60,25,.5), transparent 60%),
      linear-gradient(160deg, var(--rust-light), var(--rust) 45%, var(--rust-dark));
  }
  .ghost-circle { position: absolute; border-radius: 50%; background: var(--ghost); }

  /* Cover */
  .cover { position: absolute; left: 20px; top: 30px; width: 460px; height: 940px; }
  .cover-name {
    position: absolute; left: 60px; top: 190px; width: 360px;
    font-family: "Special Elite", "Courier New", monospace;
    font-size: 72px; line-height: .98; color: var(--cream); text-transform: uppercase;
  }
  .cover-title {
    position: absolute; left: 0; right: 0; top: 650px; text-align: center;
    font-family: "Special Elite", "Courier New", monospace;
    font-size: 22px; letter-spacing: 9px; color: var(--cream);
  }

  /* Inside page */
  .spread { position: absolute; left: 500px; top: 30px; width: 680px; height: 940px; }
  .rail { position: absolute; left: 0; top: 0; width: 220px; height: 100%; color: var(--cream); text-align: center; }
  .rail-name {
    position: absolute; left: 26px; top: 22px; width: 180px; text-align: left;
    font-family: "Special Elite", "Courier New", monospace;
    font-size: 38px; line-height: .98; color: var(--cream); text-transform: uppercase;
  }
  .rail-section { position: absolute; left: 12px; width: 200px; }
  .rail-section h2 { font-family: "Special Elite", "Courier New", monospace; font-weight: 400; font-size: 24px; margin-bottom: 8px; }
  .rail .dish { margin-bottom: 6px; }
  .rail .dish h3 { font-family: "Special Elite", "Courier New", monospace; font-weight: 400; font-size: 9px; text-transform: uppercase; color: var(--cream); }
  .rail .dish p { font-size: 8.5px; line-height: 1.15; color: var(--cream); }

  .sheet {
    position: absolute; left: 222px; top: 14px; width: 444px; height: 912px;
    background: var(--paper); padding: 14px 18px 10px;
    border-radius: 3px;
    box-shadow: inset 0 0 14px rgba(140,90,50,.35);
  }
  .sheet h2 {
    font-family: "Special Elite", "Courier New", monospace; font-weight: 400; color: var(--heading);
    font-size: 28px; text-align: center; letter-spacing: 1px; margin-bottom: 4px;
  }
  .dish h3 { font-family: "Special Elite", "Courier New", monospace; font-weight: 400; font-size: 9.5px; text-transform: uppercase; color: var(--ink); }
  .dish p { font-size: 9px; line-height: 1.2; }
  .center { text-align: center; }
  .platters .dish { margin-bottom: 8px; }
  .mains { display: flex; gap: 14px; margin-top: 4px; }
  .mains .col { flex: 1; }
  .mains .dish { margin-bottom: 7px; }
  .pasta { position: relative; margin-top: 4px; text-align: left; }
  .pasta .ghost-circle { left: 40px; top: -6px; width: 110px; height: 110px; background: rgba(169,110,70,.22); }
  .pasta p { position: relative; font-size: 9px; line-height: 1.2; margin-bottom: 4px; }
  .pasta b, .pizza-list b { font-family: "Special Elite", "Courier New", monospace; font-weight: 400; text-transform: uppercase; }
  .pizza-list p { font-size: 9px; line-height: 1.22; }
  .sides p { font-size: 9px; line-height: 1.35; text-align: center; font-family: "Special Elite", "Courier New", monospace; text-transform: uppercase; }
  .sides .plain { font-family: "Crimson Text", Georgia, serif; text-transform: none; }
  .specialty-mark {
    display: inline-block; width: 7px; height: 7px; border-radius: 50%;
    background: var(--heading); vertical-align: 1px; margin: 0 3px;
  }
  .specialty-note { margin-top: 10px; font-size: 9px; display: flex; align-items: center; gap: 3px; }
  .sheet-footer { position: absolute; left: 0; right: 0; bottom: 6px; text-align: center; font-size: 8px; }
</style>
</head>
<body>

<section class="cover rust-surface">
  <div class="ghost-circle" role="img" aria-label="Faint teapot illustration" style="left:30px;top:260px;width:180px;height:180px"></div>
  <div class="ghost-circle" role="img" aria-label="Faint bottle illustration" style="left:340px;top:60px;width:130px;height:130px"></div>
  <div class="ghost-circle" role="img" aria-label="Faint mixing bowl illustration" style="left:240px;top:400px;width:200px;height:200px"></div>
  <div class="ghost-circle" role="img" aria-label="Faint beer mug illustration" style="left:320px;top:610px;width:150px;height:150px"></div>
  <div class="ghost-circle" role="img" aria-label="Faint spoon illustration" style="left:170px;top:740px;width:170px;height:170px"></div>
  <div class="cover-name">Brass<br>Cove<br>Parlour</div>
  <div class="cover-title">DINNER&nbsp;&nbsp;&nbsp;MENU</div>
</section>

<section class="spread">
  <div class="rail rust-surface">
    <div class="ghost-circle" role="img" aria-label="Faint teapot illustration" style="left:10px;top:290px;width:120px;height:120px"></div>
    <div class="ghost-circle" role="img" aria-label="Faint mixing bowl illustration" style="left:70px;top:450px;width:150px;height:150px"></div>
    <div class="ghost-circle" role="img" aria-label="Faint spoon illustration" style="left:40px;top:780px;width:150px;height:150px"></div>

    <div class="rail-name">Brass<br>Cove<br>Parlour</div>

    <div class="rail-section" style="top:230px">
      <h2>STARTERS</h2>
      <div class="dish"><h3>Roasted Red Capsicum Soup</h3><p>with popped rice and coconut cream $9.50</p></div>
      <div class="dish"><h3>Classic Greek Salad</h3><p>cherry tomatoes, feta, kalamata olives, green capsicum &amp; cucumber $16.50</p></div>
      <div class="dish"><h3>Beetroot Salad</h3><p>slow-cooked beetroot, assorted onions, creamy goat's cheese, walnuts $17</p></div>
      <div class="dish"><h3>Beef Tartare</h3><p>hand-chopped sirloin and tenderloin mixed with capers, pickles &amp; shallots, served with bone marrow and crostini $22</p></div>
      <div class="dish"><h3>Crab Salad</h3><p>blue swimmer crab remoulade, tiger prawns, frisee salad leaves and homemade brioche melba toast $17.50</p></div>
      <div class="dish"><h3>Duck Croquettes</h3><p>crispy panko-coated duck rillettes, accompanied by parsnip mash, garlic confit and sweet wine sauce $16.50</p></div>
    </div>

    <div class="rail-section" style="top:690px">
      <h2>DESSERTS</h2>
      <div class="dish"><h3>Frozen Mojito</h3><p>lime and rum sorbet with spearmint granita, soda foam and sugar crumbs $14</p></div>
      <div class="dish"><h3>Gianduja Chocolate Fondant</h3><p>with orange coulis and lime cremoso $15</p></div>
      <div class="dish"><h3>Mango Chilli Pie</h3><p>with rice pudding ice cream and coconut sago $15</p></div>
      <div class="dish"><h3>Chocolate Cake</h3><p>with raspberry coulis, vanilla ice cream and almond brittle $15</p></div>
      <div class="dish"><h3>Hay-Infused Panna Cotta</h3><p>with spiced honey sauce and apple butter $10</p></div>
      <div class="dish"><h3>Ice Cream</h3><p>your selection, per scoop $5</p></div>
      <div class="dish"><h3>Cheese Board</h3><p>selection of three worldwide cheeses, grapes, crostini and chutney $23</p></div>
    </div>
  </div>

  <div class="sheet">
    <section class="platters center">
      <h2>PLATTERS</h2>
      <div class="dish"><h3>Seafood Platter</h3><p>selection of gravlax, smoked fish, marinated seafood,<br>pumpernickel bread and dipping sauces<br>$38 for 2 to share : $70 for 4 to share</p></div>
      <div class="dish"><h3>Charcuterie Platter <span class="specialty-mark"></span></h3><p>3 types of charcuterie, duck rillettes, pickles, crostini and<br>wholegrain mustard<br>$32 for 2 to share : $60 for 4 to share</p></div>
    </section>

    <section>
      <h2>MAIN COURSES</h2>
      <div class="mains center">
        <div class="col">
          <div class="dish"><h3>Brass Cove Parlour Burger</h3><p>200gms ground prime beef served in a home-made brioche bun with lettuce, tomato and mayo served with a side of fries $22 — top it with cheese or bacon or both, add $2 for each</p></div>
          <div class="dish"><h3>Brass Cove Parlour Bangers &amp; Mash</h3><p>prime pork sausages, buttery mashed potato covered in onion &amp; cider gravy $22</p></div>
          <div class="dish"><h3>Hay Smoked Pork Ribs</h3><p>home-smoked, slow-cooked ribs, served with spicy chimichurri sauce and fries $26</p></div>
          <div class="dish"><h3>Pan Seared Black Cod</h3><p>served on a bed of vermicelli, lemongrass, fresh chilli and kaffir lime leaves $35</p></div>
          <div class="dish"><h3>Beef Tenderloin</h3><p>200gms grilled to your choice, served with roasted vine tomatoes and red wine gravy, accompanied by buttery mashed potato or fries $35</p></div>
          <div class="dish"><h3>Brass Cove Parlour's Seafood Stew</h3><p>classic seafood stew, served in the pan with fresh black cod, prawns, calamari, clams and mussels, cooked in a prawn bisque, with bread for dipping $30</p></div>
        </div>
        <div class="col">
          <div class="dish"><h3>Roast Chicken <span class="specialty-mark"></span></h3><p>share a whole bird for 2, with jus and your choice of two sides. (Allow 25 mins to prepare) $38</p></div>
          <div class="dish"><h3>Roast Pork Belly</h3><p>served with apple compote and your choice of two sides. Whole belly shared among 3-4 people. (Allow 45 mins to roast.) $85</p></div>
          <div class="dish"><h3>Beef T-Bone</h3><p>600gms T-Bone grilled, served with red wine gravy and your choice of two sides (Shared among 2 people. Allow 25 mins to cook) $70</p></div>
          <div class="pasta">
            <div class="ghost-circle" role="img" aria-label="Faint fork illustration"></div>
            <p><b>Strigoli</b> – with beef ragu bolognese $22</p>
            <p><b>Linguini</b> – with a light creamy carbonara sauce, with smoked pancetta $23</p>
            <p><b>Rigatoni</b> – with aglio, olio and pepperoncino $20, with prawns, add $5</p>
            <p><b>Risotto</b> – with rich porcini mushrooms and crutin cheese $22</p>
            <p><b>Margherita</b> – roast tomato, mozzarella and fresh basil $24</p>
          </div>
        </div>
      </div>
    </section>

    <section class="pizza-list" style="margin-top:6px">
      <h2>PIZZAS</h2>
      <p><b>Bloody Margherita</b> – a take on the classic aperitif: vodka flushed roast tomatoes, mozzarella, celery salt, worcester and Firecrest sauces $28</p>
      <p><b>Spinach and Ricotta</b> – with toasted pine nuts, cherry tomatoes and ricotta cheese $25</p>
      <p><b>Umami Chicken</b> – with baby king oyster mushrooms, shaved parmesan and fresh thyme $27</p>
      <p><b>Parma Ham</b> – with semi-dried tomato and fresh arugula leaves $29</p>
      <p><b>Hay-Smoked Pulled Pork and Pancetta</b> – home-smoked, slow cooked pulled pork rib, with sausage, pancetta and onion $29</p>
      <p><b>Smoked Pancetta</b> – with shitake mushrooms, spring onions, chilli and brie $29</p>
      <p><span class="specialty-mark"></span><b>Seafood</b> – with smoked salmon, prawns, calamari, onions, and crushed roasted tomato $30</p>
    </section>

    <section class="sides" style="margin-top:10px">
      <h2>SIDES</h2>
      <p>Coconut corn on the cob / Onion mashed potato /<br>Peas and smoked pancetta /<br>Green beans with toasted pine nuts and garlic confit /<br>Mixed salad / Truffle fries / French fries $7<br>Bread rolls <span class="plain">– with olive oil and balsamic vinegar $4</span></p>
    </section>

    <div class="specialty-note"><span class="specialty-mark"></span> Brass Cove Parlour Specialty</div>
    <div class="sheet-footer">All prices are in Singapore Dollars and are subject to GST &amp; 10% Service Charge</div>
  </div>
</section>

</body>
</html>
```